Card design for Heating and Cooling company

this is for a heating and cooling company we recently updated our logo and need to update our cards. We attached our logo so you can incorporate it into the card. We specialize in residential and commercial furnace and air condition repairs. Have been in business since 2014.

Phone number 555.284.9137

We need the following phrases
:Repairs, Installations, and maintenance
:Quality work at reasonable prices
:residential/commercial
:Licensed &Insured
:Email Pinegrovehvac47@mailbox-example.com
Name: Teodor K (Ted)
Also on back side I would like my logo with wording :Thank you for your business and refferal

Industry/Entity Type

Hvac

Contact Information for Business Card

:residential/commercial
:Licensed & Insured
Name: Teodor K (Ted)
Number:555.284.9136

Requirements
Must have
• Blue and red colors
Nice to have
• Maybe a pic of a furnace or air conditioner

```html
<!DOCTYPE html>
<html lang="en">
<head>
<meta charset="utf-8">
<title>Pinegrove Heating &amp; Cooling — Business Card</title>
<link rel="stylesheet" href="https://fonts.googleapis.com/css2?family=Arimo:wght@400;700&display=swap">
<style>
  :root {
    --orange: #ee5a24;
    --blue: #3b4fa0;
    --frame-start: #f0602a;
    --frame-end: #3f5fb0;
    --paper: #ffffff;
    --edge: #8a8a8a;
    --thanks-1: #2a2a6a;
    --thanks-2: #d63a7a;
    --thanks-3: #8a3ab0;
    --thanks-4: #e04040;
  }
  * { box-sizing: border-box; margin: 0; padding: 0; }
  html, body { width: 1200px; height: 357px; overflow: hidden; background: var(--paper); }
  body { position: relative; font-family: "Arimo", Arial, sans-serif; }

  .card-front {
    position: absolute; left: 26px; top: 16px; width: 524px; height: 296px;
    background: linear-gradient(90deg, var(--frame-start), var(--frame-end));
    padding: 11px;
  }
  .card-front__inner {
    position: relative; width: 100%; height: 100%; background: var(--paper); overflow: hidden;
  }
  .services {
    position: absolute; left: 13px; top: 15px;
    color: var(--orange); font-size: 27px; line-height: 32.5px; list-style: none;
    white-space: nowrap;
  }
  .contact {
    position: absolute; left: 13px; top: 168px;
    color: var(--blue); font-size: 27px; line-height: 32px; list-style: none;
    white-space: nowrap;
  }
  .contact__email { font-size: 21px; }
  .brand {
    position: absolute; display: flex; align-items: center; gap: 8px;
    font-weight: 700; color: var(--blue); letter-spacing: 0.5px; white-space: nowrap;
  }
  .brand--front { left: 340px; top: 142px; font-size: 21px; }
  .brand__mark { display: block; flex: none; }

  .card-back {
    position: absolute; left: 610px; top: 2px; width: 577px; height: 329px;
    border: 1px solid var(--edge); background: var(--paper);
  }
  .brand--back { left: 0; right: 0; top: 148px; justify-content: center; font-size: 34px; }
  .thanks {
    position: absolute; left: 0; right: 0; top: 284px; text-align: center;
    font-size: 27px; line-height: 31px; white-space: nowrap;
    background: linear-gradient(90deg, var(--thanks-1), var(--thanks-2) 35%, var(--thanks-3) 65%, var(--thanks-4));
    -webkit-background-clip: text; background-clip: text; color: transparent;
  }
</style>
</head>
<body>
  <section class="card-front" aria-label="Card front">
    <div class="card-front__inner">
      <ul class="services">
        <li>Repairs, Installations and maintenance</li>
        <li>Quality work at reasonable prices</li>
        <li>Residential/commercial</li>
        <li>Licensed &amp; Insured</li>
      </ul>
      <ul class="contact">
        <li>Name: Teodor K (Ted)</li>
        <li>Number: 555.284.9137</li>
        <li class="contact__email">Email: Pinegrovehvac47@mailbox-example.com</li>
      </ul>
      <div class="brand brand--front">
        <svg class="brand__mark" width="16" height="16" viewBox="0 0 16 16" aria-hidden="true"><circle cx="8" cy="8" r="8" fill="var(--blue)"/></svg>
        <span>PINEGROVE</span>
      </div>
    </div>
  </section>

  <section class="card-back" aria-label="Card back">
    <div class="brand brand--back">
      <svg class="brand__mark" width="24" height="24" viewBox="0 0 24 24" aria-hidden="true"><circle cx="12" cy="12" r="12" fill="var(--blue)"/></svg>
      <span>PINEGROVE</span>
    </div>
    <p class="thanks">Thank you for your business and refferal</p>
  </section>
</body>
</html>
```